Business card for Tolvery Anesthesia LLC

This is for a business care for Tolvery Anesthesia LLC. Dr. Lisbeth Tolvery, CRNA, DNAP is the sole provider in the LLC. Business address is 4718 N Brackley Street,
Oakhaven, PA 17342
CRNA stands for certified registered nurse anesthetist
"Keeping you safe and comfortable"
I plan to give this business card to the patients that I provide anesthesia to.
Creative design that ties into Anesthesia. Calm soothing colors.

Target Market(s)

Business card for my patients.

Industry/Entity Type

Medicine

Contact Information for Business Card

Creative, professional, eye catching

Logo Text

Tolvery Anesthesia

Font styles to use
Serif
Script

Colors

Designer to choose colors to be used in the design.

Requirements
Must have
• Tolvery Anesthesia
• Dr. Lisbeth Tolvery, CRNA, DNAP
• tolvery.anesthesia@ quillmail.net
Nice to have
• "Keeping you safe and comfortable"
Should not have
• phone number

```html
<!DOCTYPE html>
<html lang="en">
<head>
<meta charset="utf-8">
<title>Tolvery Anesthesia – Business Card</title>
<link rel="stylesheet" href="https://fonts.googleapis.com/css2?family=Anton&family=Questrial&display=swap">
<style>
  :root {
    --backdrop: #2b2d30;
    --card-white: #ffffff;
    --ink: #111111;
    --brand-deep: #0f3d3a;
    --tagline-teal: #3f8f8a;
    --band-cream: #f6ead3;
    --band-mist: #e1e4cf;
    --band-sage: #c4cfb0;
    --band-teal: #3d9a8e;
    --band-pine: #236259;
    --band-forest: #174a44;
    --portrait-coral: #ee5b57;
  }
  * { margin: 0; padding: 0; box-sizing: border-box; }
  html, body {
    width: 1200px; height: 900px; overflow: hidden;
    background: var(--backdrop);
  }
  .canvas {
    position: relative; width: 1200px; height: 900px;
    display: flex; align-items: center; justify-content: center;
  }
  .business-card {
    position: relative; width: 1050px; height: 600px;
    background: var(--card-white);
    border-radius: 36px; overflow: hidden;
    box-shadow: 0 18px 40px rgba(0,0,0,.45);
  }
  .color-bands { position: absolute; inset: 0; width: 100%; height: 100%; }
  .portrait-placeholder {
    position: absolute; left: 95px; top: 40px;
    width: 210px; height: 210px; border-radius: 50%;
    background: radial-gradient(circle at 50% 60%, #f3f3f3 0 34%, var(--portrait-coral) 35%);
  }
  .brand-name {
    position: absolute; left: 330px; top: 28px;
    font-family: "Anton", sans-serif; font-size: 84px; line-height: 1;
    color: var(--brand-deep); letter-spacing: 1px; text-transform: uppercase;
  }
  .tagline {
    position: absolute; left: 336px; top: 128px;
    font-family: "Questrial", sans-serif; font-size: 32px;
    color: var(--tagline-teal);
  }
  .provider-name {
    position: absolute; left: 150px; top: 278px;
    font-family: "Questrial", sans-serif; font-size: 40px; color: var(--ink);
  }
  .contact-list {
    position: absolute; left: 110px; top: 360px; list-style: none;
    font-family: "Questrial", sans-serif; font-size: 32px; color: var(--ink);
    line-height: 1.3;
  }
  .contact-item { display: flex; align-items: flex-start; gap: 14px; margin-bottom: 10px; }
  .contact-icon { width: 24px; height: 24px; margin-top: 6px; flex: none; }
</style>
</head>
<body>
<main class="canvas">
  <article class="business-card">
    <svg class="color-bands" viewBox="0 0 1050 600" aria-hidden="true">
      <polygon points="640,0 1050,0 1050,600 560,600" fill="var(--band-cream)"/>
      <polygon points="710,0 1050,0 1050,600 630,600" fill="var(--band-mist)"/>
      <polygon points="780,0 1050,0 1050,600 700,600" fill="var(--band-sage)"/>
      <polygon points="850,0 1050,0 1050,600 770,600" fill="var(--band-teal)"/>
      <polygon points="920,0 1050,0 1050,600 840,600" fill="var(--band-pine)"/>
      <polygon points="990,0 1050,0 1050,600 910,600" fill="var(--band-forest)"/>
    </svg>

    <div class="portrait-placeholder" role="img" aria-label="Illustration of a doctor with a stethoscope in a coral circle"></div>

    <h1 class="brand-name">Tolvery Anesthesia</h1>
    <p class="tagline">Keeping you safe and comfortable</p>

    <h2 class="provider-name">Dr. Lisbeth Tolvery, CRNA, DNAP</h2>

    <ul class="contact-list">
      <li class="contact-item">
        <svg class="contact-icon" viewBox="0 0 24 24" aria-hidden="true">
          <path d="M12 2a7 7 0 0 0-7 7c0 5 7 13 7 13s7-8 7-13a7 7 0 0 0-7-7z" fill="var(--ink)"/>
          <circle cx="12" cy="9" r="2.8" fill="var(--card-white)"/>
        </svg>
        <span>4718 N Brackley Street,<br>Oakhaven, PA 17342</span>
      </li>
      <li class="contact-item">
        <svg class="contact-icon" viewBox="0 0 24 24" aria-hidden="true">
          <circle cx="12" cy="12" r="9" fill="var(--ink)"/>
          <rect x="7" y="9" width="10" height="7" fill="var(--card-white)"/>
        </svg>
        <span>tolvery.anesthesia@ quillmail.net</span>
      </li>
    </ul>
  </article>
</main>
</body>
</html>
```